Clean, Crisp, and Modern App User Interface

I've created the basic App interface, but it could use a face-lift to make it look more modern, clean, crisp.
Its a chat bot app with a humorous, cartoony look. Take a look! Will be a fun project to work on :)
Required UI Elements:
-- Character Portrait
-- Chat Conversation area (designed to be scroll-able, by swipe)
-- Text in the chat (choose a text that looks great)
-- Push-to-talk microphone button, with changed graphic when pressed
-- An arrow, that when pressed will flip the character around..put it where you think is best
-- A settings button
-- A credits count text and credits token
-- A thinking icon/animation. (Animates to fill up when 100% complete)
-- A character level button, pressed takes you to unlocks menu
-- Background (any color, but I kinda like the green one I picked)
Final product must be supplied in layered .psd
Think like these examples:
http://www.tackvolo.com/glimrabox/mob-9-scr-layouts/

```html
<!DOCTYPE html>
<html lang="en">
<head>
<meta charset="utf-8">
<title>Chat Bot App Screen</title>
<link href="https://fonts.googleapis.com/css2?family=Luckiest+Guy&family=Kalam:wght@700&family=Roboto:wght@400;500&display=swap" rel="stylesheet">
<style>
  :root {
    --page-bg: #98bf3f;
    --bar-orange: #f6ae1a;
    --title-white: #ffffff;
    --chat-green-light: #b8d46a;
    --chat-green: #7fa83a;
    --chat-green-dark: #5d8a2c;
    --stage-green: #4f8a2a;
    --stage-green-dark: #2f5f1c;
    --scroll-yellow: #e8b21a;
    --pill-green: #6f9a36;
    --arrow-green: #a9cf55;
    --badge-red: #e8262b;
    --text-dark: #1a1a1a;
    --mic-circle: rgba(30, 30, 30, 0.78);
  }
  * { margin: 0; padding: 0; box-sizing: border-box; }
  html, body { width: 1017px; height: 1200px; overflow: hidden; }
  body { background: var(--page-bg); position: relative; font-family: 'Kalam', sans-serif; }

  .app-screen {
    position: absolute; left: 188px; top: 32px;
    width: 640px; height: 1136px; overflow: hidden;
    box-shadow: 0 20px 50px rgba(0,0,0,0.25);
  }

  .status-bar {
    position: absolute; left: 0; top: 0; width: 640px; height: 40px;
    background: var(--bar-orange); color: #fff;
    font-family: 'Roboto', sans-serif; font-size: 22px; font-weight: 500;
  }
  .status-left { position: absolute; left: 14px; top: 7px; display: flex; align-items: center; gap: 8px; }
  .status-time { position: absolute; left: 0; right: 0; top: 7px; text-align: center; }
  .status-right { position: absolute; right: 14px; top: 7px; display: flex; align-items: center; gap: 8px; }

  .nav-bar {
    position: absolute; left: 0; top: 40px; width: 640px; height: 108px;
    background: var(--bar-orange);
  }
  .nav-title {
    position: absolute; left: 0; right: 0; top: 32px; text-align: center;
    font-family: 'Luckiest Guy', sans-serif; font-size: 50px; font-weight: 400;
    color: var(--title-white); text-transform: uppercase;
    letter-spacing: 1px; line-height: 1;
  }
  .settings-button { position: absolute; left: 22px; top: 30px; width: 50px; height: 50px; }
  .credits-button { position: absolute; right: 22px; top: 28px; width: 64px; height: 60px; }
  .credits-badge {
    position: absolute; right: 0; top: 0; width: 28px; height: 28px; border-radius: 50%;
    background: var(--badge-red); color: #fff; font-family: 'Roboto', sans-serif;
    font-size: 17px; font-weight: 500; text-align: center; line-height: 28px;
  }

  .chat-area {
    position: absolute; left: 0; top: 148px; width: 640px; height: 546px;
    background: radial-gradient(ellipse at 25% 55%, var(--chat-green-light) 0%, var(--chat-green) 55%, var(--chat-green-dark) 100%);
  }
  .scroll-indicator {
    position: absolute; right: 8px; top: 44px; width: 6px; height: 236px;
    border-radius: 3px; background: var(--scroll-yellow);
  }
  .message { position: absolute; display: flex; align-items: flex-start; gap: 12px; font-size: 28px; line-height: 34px; }
  .message-bot { left: 26px; color: #fff; }
  .message-user { right: 28px; color: var(--text-dark); flex-direction: row-reverse; text-align: right; }
  .avatar { width: 58px; height: 58px; border-radius: 50%; flex: none; }
  .avatar-bot { background: radial-gradient(circle, #9a6fc0 0%, #e0763a 100%); border: 2px solid rgba(255,255,255,0.6); }
  .avatar-user { background: radial-gradient(circle, #4a4a4a 0%, #c9d5d9 100%); border: 2px solid rgba(255,255,255,0.6); }
  .message-text { padding-top: 8px; }

  .thinking-indicator {
    position: absolute; left: 22px; top: 450px; width: 180px; height: 68px;
    border-radius: 34px; background: var(--pill-green);
    display: flex; align-items: center; padding-left: 26px; gap: 16px;
  }
  .thinking-dot { width: 14px; height: 14px; border-radius: 50%; background: #fff; }

  .character-stage {
    position: absolute; left: 0; top: 694px; width: 640px; height: 442px;
    background: radial-gradient(ellipse at 50% 20%, var(--stage-green) 0%, var(--stage-green-dark) 100%);
  }
  .character-portrait {
    position: absolute; left: 120px; top: 30px; width: 400px; height: 412px;
    border-radius: 200px 200px 0 0;
    background: linear-gradient(180deg, #e4702a 0%, #e9a77e 40%, #5b2f6d 80%, #3a1e48 100%);
    opacity: 0.85;
  }
  .flip-arrow { position: absolute; top: 196px; width: 30px; height: 56px; }
  .flip-arrow-left { left: 20px; }
  .flip-arrow-right { right: 20px; }
  .mic-button {
    position: absolute; left: 240px; top: 250px; width: 160px; height: 160px; border-radius: 50%;
    background: var(--mic-circle); display: flex; align-items: center; justify-content: center;
  }
</style>
</head>
<body>
  <main class="app-screen">
    <header class="status-bar">
      <div class="status-left">
        <svg width="64" height="14" viewBox="0 0 64 14" aria-hidden="true">
          <circle cx="6" cy="7" r="5" fill="#fff"/><circle cx="19" cy="7" r="5" fill="#fff"/>
          <circle cx="32" cy="7" r="5" fill="#fff"/><circle cx="45" cy="7" r="5" fill="#fff"/>
          <circle cx="58" cy="7" r="4.5" fill="none" stroke="#fff" stroke-width="1.2"/>
        </svg>
        <span>Vexa</span>
        <svg width="24" height="18" viewBox="0 0 24 18" aria-hidden="true">
          <path d="M2 6a14 14 0 0 1 20 0M5.5 9.5a9 9 0 0 1 13 0M9 13a4 4 0 0 1 6 0" fill="none" stroke="#fff" stroke-width="2.2" stroke-linecap="round"/>
          <circle cx="12" cy="16" r="1.6" fill="#fff"/>
        </svg>
      </div>
      <div class="status-time">4:20 PM</div>
      <div class="status-right">
        <svg width="20" height="20" viewBox="0 0 20 20" aria-hidden="true">
          <circle cx="10" cy="10" r="7.5" fill="none" stroke="#fff" stroke-width="2"/>
          <path d="M10 5v5l3 2" stroke="#fff" stroke-width="2" fill="none"/>
        </svg>
        <span>100%</span>
        <svg width="46" height="20" viewBox="0 0 46 20" aria-hidden="true">
          <rect x="1" y="1" width="40" height="18" rx="3" fill="#fff" stroke="#fff"/>
          <rect x="42" y="6" width="3" height="8" rx="1" fill="#fff"/>
        </svg>
      </div>
    </header>

    <nav class="nav-bar">
      <svg class="settings-button" viewBox="0 0 50 50" aria-label="Settings">
        <g fill="#fff">
          <rect x="21" y="2" width="8" height="10" rx="1"/><rect x="21" y="38" width="8" height="10" rx="1"/>
          <rect x="2" y="21" width="10" height="8" rx="1"/><rect x="38" y="21" width="10" height="8" rx="1"/>
          <rect x="21" y="2" width="8" height="10" rx="1" transform="rotate(45 25 25)"/>
          <rect x="21" y="38" width="8" height="10" rx="1" transform="rotate(45 25 25)"/>
          <rect x="2" y="21" width="10" height="8" rx="1" transform="rotate(45 25 25)"/>
          <rect x="38" y="21" width="10" height="8" rx="1" transform="rotate(45 25 25)"/>
        </g>
        <circle cx="25" cy="25" r="14" fill="none" stroke="#fff" stroke-width="5"/>
        <circle cx="25" cy="25" r="5" fill="#fff"/>
      </svg>
      <h1 class="nav-title">Chat Bot</h1>
      <div class="credits-button" aria-label="Credits: 5">
        <svg width="56" height="56" viewBox="0 0 56 56" style="position:absolute;left:0;top:4px" aria-hidden="true">
          <circle cx="26" cy="28" r="22" fill="none" stroke="#fff" stroke-width="4"/>
          <circle cx="26" cy="28" r="15" fill="none" stroke="#fff" stroke-width="2"/>
          <path d="M30 20c-2-2-9-2-9 2s9 3 9 7-7 4-9 2M25.5 16v24" fill="none" stroke="#fff" stroke-width="2.6" stroke-linecap="round"/>
        </svg>
        <span class="credits-badge">5</span>
      </div>
    </nav>

    <section class="chat-area" aria-label="Conversation">
      <div class="scroll-indicator"></div>

      <div class="message message-bot" style="top:36px">
        <div class="avatar avatar-bot" role="img" aria-label="Chat character avatar"></div>
        <p class="message-text">Good morning, dear.</p>
      </div>
      <div class="message message-user" style="top:110px">
        <div class="avatar avatar-user" role="img" aria-label="User avatar"></div>
        <p class="message-text">Why are you so ugly?</p>
      </div>
      <div class="message message-bot" style="top:190px">
        <div class="avatar avatar-bot" role="img" aria-label="Chat character avatar"></div>
        <p class="message-text">Now that's not a very nice thing<br>to say to your Aunt Bea Bea.</p>
      </div>
      <div class="message message-user" style="top:302px">
        <div class="avatar avatar-user" role="img" aria-label="User avatar"></div>
        <p class="message-text">What is the main ingredient in cake?</p>
      </div>

      <div class="thinking-indicator" aria-label="Thinking">
        <svg width="34" height="38" viewBox="0 0 34 38" aria-hidden="true">
          <path d="M17 2C8 2 2 8 2 16c0 5 2 8 5 10v10h14v-5h5a3 3 0 0 0 3-3v-5l4-1-4-7C29 7 24 2 17 2z" fill="#fff"/>
          <circle cx="15" cy="15" r="5" fill="none" stroke="#6f9a36" stroke-width="2.5"/>
        </svg>
        <span class="thinking-dot"></span><span class="thinking-dot"></span><span class="thinking-dot"></span>
      </div>
    </section>

    <section class="character-stage">
      <div class="character-portrait" role="img" aria-label="Cartoon character portrait: an aunt with curly orange hair, cat-eye glasses and purple outfit"></div>
      <svg class="flip-arrow flip-arrow-left" viewBox="0 0 30 56" aria-label="Flip character left">
        <path d="M26 4 6 28l20 24" fill="none" stroke="var(--arrow-green)" stroke-width="5" stroke-linecap="round" stroke-linejoin="round"/>
      </svg>
      <svg class="flip-arrow flip-arrow-right" viewBox="0 0 30 56" aria-label="Flip character right">
        <path d="M4 4l20 24L4 52" fill="none" stroke="var(--arrow-green)" stroke-width="5" stroke-linecap="round" stroke-linejoin="round"/>
      </svg>
      <div class="mic-button" aria-label="Push to talk">
        <svg width="64" height="96" viewBox="0 0 64 96" aria-hidden="true">
          <rect x="18" y="2" width="28" height="54" rx="14" fill="#fff"/>
          <path d="M6 40a26 26 0 0 0 52 0" fill="none" stroke="#fff" stroke-width="6" stroke-linecap="round"/>
          <path d="M32 66v18M18 88h28" stroke="#fff" stroke-width="6" stroke-linecap="round"/>
        </svg>
      </div>
    </section>
  </main>
</body>
</html>
```